GUARANTEED! - Creation of Lumora Promotional Images (requires Photoshops to modify cars)

Hi all,

We will require 5 different images to be created although once the first one is completed, the look and theme can literally be copied across to the others. These promotional images are to represent the service our website offers as well as the benefit’s the user can receive. (please ask for the website via private message if required) Our website is literally a comparison website related to vehicle modifications - so we make it quick and easy for users to find the best deal with local Window Tinters, ECU Remappers, Alloy Wheel Refurbs & More.

Aim of the image - This is purely to be posted on lumora to push viewers to our website / lumora page (there will be links in the description when it’s posted on lumora) so the image needs to tell the user what we do and urge them to visit the website.

Target market - our target market is mainly the car enthusiast (ages between 17 - 25) although we’re looking to keep this promotional image simple, professional and with the use of light neutral colours.

Image to be created - (our idea, please feel free to change) - see attachment of rough sketch created titled : ‘Rough Sketch Promotional Image

Main title across the top will read ‘FIND THE BEST DEAL WITH :’ - The words best deal should stand out more and be of a larger font / potentially different colour, maybe orange to keep in theme with the website. Then as shown in the sketch, we will have car number 1 which has been photoshopped as stated further down . Then we will have arrows pointing onto the car which will state the different modifications that has been completed on the car e.g - arrow will point to the rear window and will state the words :

WINDOW TINTERS
IN YOUR AREA

(regarding the text stated above, we feel it would be best if they were all placed the same distance away from the car to keep the professional look) - we also feel the service mentioned such as ‘WINDOW TINTERS’ should be a larger font than the ‘IN YOUR AREA’

Each car will have 4 arrows pointing on different parts of the car with text added as stated above (hopefully the rough sketch will make all these requirements that little bit clearer)

Then underneath the car image with the 4 arrows and text, we will have a Call to action button (which should keep the same kind of theme as that on the website homepage, (green blackground of block with white text) - The text in this button will read ‘CLICK BELOW!’ - we also had the idea of adding an arrow under the Call to action button to point the users to the description below the image. (Needs to be clear space around the CTA so it stands out - apart from potentially this arrow)

Then finally we’d like to have our logo (quite small) to the bottom left of the image with the words ‘PLEASE SHARE!’ to the bottom right of the image.

As you can see, the requirements we’re after are quite simple so the time will be mostly in the photoshopping of the 5 cars.

Please refer to the rough sketch but if you have any questions, please contact us here.

PHOTOSHOPS REQUIRED

The changes made to each car will be partly left up to you - however it’s vitally important that it stands out yet doesn’t look ‘silly’ and needs to look realistic - looking realistic is important.

Photoshop requirements

Car 1 - Green Valtero

- Possibly change colour - please feel free to try other colours (need to look realistic)
- Change the colour of the rear window to a limo style black.
- Change the colour of the roof (can only see a slight bit of it) to black
- Change the colour of the wheels (the colour used here will depend on the change colour of the actual car, some options we like include yellow, green, orange and red

Car 2 - White Korvel ZX

- Change the colour of the rear window and rear side window to a limo style black
- Change the colour of the roof to black (not decided whether it should be black/matt black so test)
- Change the colour of the wheels to a red/ orange

Car 3 - Blue Brenn

- Possibly change colour - please feel free to try other colours - maybe a red but needs to look realistic
- Change the colour of the rear window visible to a limo style black
- Change the colour of the roof to black
- Change the colour of the wheels to black

Car 4 - Yellow Korvel ZX

- Please try changing the colour of this to a metallic grey/dark silver / gloss dark blue.
- Change the colour of the wheels to a yellow

Car 5 - Black Korvel ZX (first of all we need to remove the background of this image)

Please state if this is too difficult to photoshop and we’ll go from there.

- Colour change to red please - ensure looks realistic
- Change the colour of the wheels to a black

If any of the changes we’ve requested don’t look realistic when you’ve created them - please let us know and feel free to try other colours … remember, needs to look professional and realistic.

Background - up to you although we feel something quite neutral would work well - please however try out whatever you think would look good.

************* IMPORTANT - PLEASE READ *******************

To save you time and to avoid wasted effort, we'd like you to create the promotional image using image 1 ONLY first of all - once we're satisfied with that 100%, we would then ask you to complete the other 4 images (which shouldn't take long once the first image is complete)

*************************************************************************

Just to add - we have purchased the rights for these images but if you feel you've some car images that would suit our requirements better than these, please send them across to us for our opinion.

We may add to this brief so keep an eye out - we will also offer additional work to the winning designer - if you have any questions at all, please ask away.

Thanks,

Owen,

Still not there with the design all - keep them coming.Thanks Added Saturday, October 1, 2016

Project Deadline Extended Reason: Not happy with the designs receivec and only received a few different designers whereas the project I purchased stated I would receive alot more..Not impressed so far.Regards.Owen Added Monday, October 3, 2016

Car enthusiast / youthful - but needs to have the professional clear look - most important.

Promotional

Serif
Sans Serif

• - Title of 'FIND THE BEST DEAL WITH : '
• - Car image for each
• - 4 Arrows coming off car for each image with the text stated
• - Call to action button - that stands out
• - Logo and words 'Please share!' / 'Please share me!'
• Potential other car images (would need commercial right so would have to be free for commercial use or a suitable price to pay for the rights) - this is only if you feel you have an image that would be better than those we currently have.
• Needs to be kept clear - points to stand out are the opening title of 'FIND THE BEST DEAL WITH :', Car and the service such as 'WINDOW TINTERS'

```html
<!DOCTYPE html>
<html lang="en">
<head>
<meta charset="utf-8">
<title>Find the Best Deal</title>
<link rel="stylesheet" href="https://fonts.googleapis.com/css2?family=Barlow+Condensed:ital,wght@1,700;1,800;1,900&family=Archivo:ital,wght@1,600;1,800&family=Roboto:ital@1&display=swap">
<style>
  :root {
    --ink: #0c0c0c;
    --slate: #4f5358;
    --muted: #5d6166;
    --orange: #f58a1f;
    --orange-dark: #d96d0c;
    --green: #4cbf27;
    --green-dark: #2f9a14;
    --green-light: #7fdc4c;
    --white: #ffffff;
  }
  * { margin: 0; padding: 0; box-sizing: border-box; }
  html, body { width: 1200px; height: 905px; overflow: hidden; background: var(--white); }
  .poster { position: relative; width: 1200px; height: 905px; background: var(--white); }

  .headline {
    position: absolute; top: 38px; left: 0; width: 1200px; text-align: center;
    font-family: "Barlow Condensed", sans-serif; font-style: italic; font-weight: 900;
    color: var(--slate); font-size: 92px; line-height: 1; letter-spacing: 1px; white-space: nowrap;
  }
  .headline .accent { color: var(--orange); font-size: 118px; margin: 0 10px; }

  .vehicle-photo {
    position: absolute; left: 332px; top: 312px; width: 535px; height: 215px;
    border-radius: 48% 40% 22% 26% / 60% 55% 30% 30%;
    background: radial-gradient(ellipse at 55% 45%, #52e23a 0%, #3fcf22 55%, #2a2a2a 100%);
  }

  .service {
    position: absolute; font-family: "Archivo", sans-serif; font-style: italic; text-align: center;
  }
  .service .name { display: block; font-weight: 800; font-size: 28px; color: var(--ink); letter-spacing: 0.5px; }
  .service .area { display: block; font-weight: 800; font-size: 21px; color: var(--muted); margin-top: 8px; letter-spacing: 0.5px; }
  .service--tint { left: 62px; top: 236px; width: 276px; }
  .service--roof { left: 763px; top: 236px; width: 370px; }
  .service--wheel { left: 66px; top: 564px; width: 418px; }
  .service--ecu { left: 862px; top: 564px; width: 280px; }

  .pointers { position: absolute; left: 0; top: 0; width: 1200px; height: 905px; }

  .cta { position: absolute; left: 403px; top: 712px; width: 470px; height: 150px; }
  .cta-label {
    position: absolute; left: 403px; top: 728px; width: 470px; text-align: center;
    font-family: "Barlow Condensed", sans-serif; font-style: normal; font-weight: 800;
    color: var(--white); line-height: 1;
  }
  .cta-label .lead { display: block; font-size: 38px; letter-spacing: 1px; }
  .cta-label .now { display: block; font-family: "Archivo", sans-serif; font-style: normal; font-weight: 800; font-size: 66px; margin-top: 0; }

  .brand {
    position: absolute; left: 32px; top: 854px;
    font-family: "Archivo", sans-serif; font-style: italic; font-weight: 800;
    font-size: 22px; color: var(--slate); letter-spacing: 0.5px;
  }
  .share {
    position: absolute; left: 1010px; top: 848px; width: 175px; height: 40px;
    border: 1px solid var(--slate); display: flex; align-items: center; justify-content: center;
    font-family: "Roboto", sans-serif; font-style: italic; font-size: 19px; color: var(--slate);
  }
</style>
</head>
<body>
<main class="poster">
  <h1 class="headline">FIND THE <span class="accent">BEST DEAL</span> WITH</h1>

  <div class="vehicle-photo" role="img" aria-label="Bright green sports hatchback with tinted windows, black roof and dark alloy wheels"></div>

  <svg class="pointers" viewBox="0 0 1200 905" aria-hidden="true">
    <g fill="var(--orange)">
      <path d="M204 318 C 220 345, 255 350, 288 348 L 285 336 L 308 352 L 288 366 L 288 357 C 250 360, 215 352, 200 322 Z"/>
      <path d="M758 272 C 735 262, 700 266, 680 282 L 687 290 L 658 296 L 668 270 L 674 277 C 700 258, 738 258, 760 268 Z"/>
      <path d="M258 548 C 245 530, 255 505, 284 500 L 282 490 L 306 504 L 286 518 L 285 509 C 262 513, 255 528, 264 546 Z"/>
      <path d="M952 546 C 960 525, 948 505, 922 500 L 923 490 L 902 502 L 920 518 L 921 509 C 942 513, 950 528, 946 544 Z"/>
    </g>
  </svg>

  <div class="service service--tint"><span class="name">WINDOW TINTERS</span><span class="area">IN YOUR AREA</span></div>
  <div class="service service--roof"><span class="name">ROOF VINYL WRAPPERS</span><span class="area">IN YOUR AREA</span></div>
  <div class="service service--wheel"><span class="name">ALLOY WHEEL REFURBERS</span><span class="area">IN YOUR AREA</span></div>
  <div class="service service--ecu"><span class="name">ECU REMAPPERS</span><span class="area">IN YOUR AREA</span></div>

  <svg class="cta" viewBox="0 0 470 150" aria-hidden="true">
    <defs>
      <linearGradient id="ctaFill" x1="0" y1="0" x2="0" y2="1">
        <stop offset="0" stop-color="var(--green-light)"/>
        <stop offset="1" stop-color="var(--green-dark)"/>
      </linearGradient>
    </defs>
    <path d="M8 96 L 235 148 L 462 96 L 462 104 L 235 150 L 8 104 Z" fill="var(--green-dark)"/>
    <path d="M8 84 L 235 134 L 462 84 L 462 92 L 235 142 L 8 92 Z" fill="var(--green)"/>
    <path d="M8 6 Q 8 0 14 0 L 456 0 Q 462 0 462 6 L 462 78 L 235 128 L 8 78 Z" fill="url(#ctaFill)" stroke="var(--green-dark)" stroke-width="2"/>
  </svg>
  <div class="cta-label"><span class="lead">SEARCH FOR FREE</span><span class="now">NOW</span></div>

  <div class="brand">TUNEWISE MOTORS</div>
  <div class="share">PLEASE SHARE</div>
</main>
</body>
</html>
```